Business Card and Letterhead for Nurlo - modern real estate business

I need a double sided business card design for Nurlo. Please see business card brief here https://papers.trelvimo.net/sheet/q/7XrTbaLeZpMmQ2uWvd9HkCj4yNoEfsGi3lRtAz_pk/view?mode=shared

Please feel free to design the business cards however you feel best. I am happy to give some creative freedoms and then provide feedback from there.

Please then also create a letterhead to match the business card design

Colors

Designer to choose colors to be used in the design.

Requirements
Must have
• Must be a modern, elegant business card which looks very professional

```html
<!DOCTYPE html>
<html lang="en">
<head>
<meta charset="utf-8">
<title>Nurlo Business Card</title>
<link rel="stylesheet" href="https://fonts.googleapis.com/css2?family=Barlow+Condensed:wght@400;500;700&display=swap">
<style>
  :root {
    --brand-red: #d70c2c;
    --paper-white: #f7f7f7;
    --backdrop: #e4e4e4;
    --card-shadow: rgba(0, 0, 0, 0.14);
  }
  * { box-sizing: border-box; margin: 0; padding: 0; }
  html, body {
    width: 1200px;
    height: 675px;
    overflow: hidden;
    background: var(--backdrop);
    font-family: "Barlow Condensed", sans-serif;
  }
  .stage {
    position: relative;
    width: 1200px;
    height: 675px;
    display: flex;
    align-items: center;
    justify-content: center;
    gap: 60px;
  }
  .card {
    position: relative;
    width: 420px;
    height: 240px;
    box-shadow: 0 10px 30px var(--card-shadow);
  }
  .card-front {
    background: var(--brand-red);
    display: flex;
    align-items: center;
    justify-content: center;
  }
  .front-wordmark {
    color: var(--paper-white);
    font-weight: 700;
    font-size: 76px;
    letter-spacing: 6px;
    line-height: 1;
  }
  .card-back {
    background: var(--paper-white);
    color: var(--brand-red);
  }
  .agent-details {
    position: absolute;
    left: 28px;
    top: 24px;
    font-size: 11px;
    line-height: 1.45;
    font-weight: 400;
  }
  .agent-name {
    font-size: 18px;
    font-weight: 500;
    line-height: 1.2;
    margin-bottom: 2px;
  }
  .divider-line {
    position: absolute;
    left: 28px;
    right: 28px;
    top: 124px;
    height: 1.5px;
    background: var(--brand-red);
  }
  .back-wordmark {
    position: absolute;
    right: 28px;
    top: 94px;
    font-size: 30px;
    font-weight: 700;
    letter-spacing: 2px;
    line-height: 1;
  }
  .office-details {
    position: absolute;
    right: 28px;
    top: 134px;
    text-align: right;
    font-size: 11px;
    line-height: 1.45;
    font-weight: 400;
  }
</style>
</head>
<body>
  <main class="stage">
    <section class="card card-front" aria-label="Business card front">
      <div class="front-wordmark">NURLO</div>
    </section>

    <section class="card card-back" aria-label="Business card back">
      <div class="agent-details">
        <div class="agent-name">Dana Merritt</div>
        <div>Licenced Real Estate Agent</div>
        <div>Lic No. 20481157</div>
        <div>0400 318 204</div>
        <div>dana@nurlo.com</div>
      </div>
      <div class="back-wordmark">NURLO</div>
      <div class="divider-line"></div>
      <div class="office-details">
        <div>Lic No. 10074412</div>
        <div>PO Box 1190</div>
        <div>Larkfield NSW 2990</div>
        <div>02 5510 3478</div>
        <div>info@nurlo.com</div>
        <div>www.nurlo.com</div>
      </div>
    </section>
  </main>
</body>
</html>
```